Tindarra Business Card Design

We would like to design a business card that has a rural flare to it with blue colouring somewhere in the design. We would also like to include our cattle's symbol brand as part of the logo.

Tindarra Stud is our stud cattle business along with our commercial cattle feedlot we also sale hay.

Industry/Entity Type

Business

Contact Information for Business Card

Tindarra Charolais
Dean & Rosalind Hockley
PO Box 318 Wirralong Qld 4791
57 Hockley's Rd Old Tindarra Qld 4791
E: drhock@fencelinemail.com.au
P: 07 49372058
M: Dean 0417295846
M: Rosalind 0439184702

```html
<!DOCTYPE html>
<html lang="en">
<head>
<meta charset="utf-8">
<title>Tindarra Business Card Design</title>
<link href="https://fonts.googleapis.com/css2?family=Roboto:wght@300;400;700&display=swap" rel="stylesheet">
<style>
  :root {
    --sky: #1fb6ea;
    --sky-light: #5fd0f5;
    --field: #12a54e;
    --paper: #ffffff;
    --paper-shade: #eeeeee;
    --ink-grey: #a7a9ac;
    --ink-dark: #6d6e71;
    --cattle: #e4e4e4;
    --backdrop: #efe9df;
  }
  * { margin: 0; padding: 0; box-sizing: border-box; }
  html, body { width: 1200px; height: 1023px; overflow: hidden; }
  body {
    background: var(--backdrop);
    font-family: "Roboto", Arial, sans-serif;
    position: relative;
  }
  .card {
    position: absolute;
    width: 620px;
    height: 379px;
    overflow: hidden;
    box-shadow: 0 6px 18px rgba(0,0,0,0.18);
  }
  .brand {
    position: absolute;
    display: flex; align-items: center; gap: 14px;
    white-space: nowrap;
  }
  .brand-mark { width: 14px; height: 14px; border-radius: 50%; flex: none; }
  .brand-name {
    font-weight: 700; font-size: 30px; line-height: 1; letter-spacing: 1px;
    text-transform: uppercase;
  }

  /* Front */
  .card-front { left: 50px; top: 60px; background: var(--field); }
  .front-sky { position: absolute; left: 0; top: 0; width: 100%; height: 100%; }
  .card-front .brand { left: 60px; top: 72px; color: var(--paper); }
  .card-front .brand-mark { background: var(--paper); }
  .cattle-illustration {
    position: absolute; left: 70px; top: 170px; width: 250px; height: 200px;
    background: var(--cattle); border-radius: 40px 60px 20px 20px;
  }

  /* Back */
  .card-back {
    left: 530px; top: 580px;
    background: linear-gradient(135deg, var(--paper) 55%, var(--paper-shade));
  }
  .card-back .brand { left: 50px; top: 56px; color: var(--ink-grey); }
  .card-back .brand-mark { background: var(--ink-grey); }
  .holder {
    position: absolute; right: 46px; top: 72px;
    font-weight: 300; font-size: 26px; color: var(--ink-dark); letter-spacing: 0.5px;
    padding-top: 8px; border-top: 1px solid var(--ink-grey);
    width: 210px; text-align: right; white-space: nowrap;
  }
  .divider {
    position: absolute; left: 40px; right: 40px; top: 160px; height: 1px; background: var(--ink-grey);
  }
  .contacts {
    position: absolute; left: 40px; top: 178px; list-style: none;
    font-size: 15px; color: var(--ink-dark); line-height: 26px;
  }
  .contacts li { display: flex; align-items: center; gap: 10px; white-space: nowrap; }
  .contact-icon {
    width: 18px; height: 18px; background: var(--field); border-radius: 3px;
    display: inline-flex; align-items: center; justify-content: center; flex: none;
  }
  .contact-icon svg { width: 12px; height: 12px; }
  .contact-icon.blank { background: transparent; }
  .back-strip {
    position: absolute; left: 0; bottom: 0; width: 100%; height: 22px; background: var(--field);
  }
</style>
</head>
<body>

<section class="card card-front">
  <svg class="front-sky" viewBox="0 0 620 379" preserveAspectRatio="none" aria-hidden="true">
    <defs>
      <linearGradient id="skyTone" x1="0" y1="0" x2="0" y2="1">
        <stop offset="0" stop-color="#5fd0f5"/>
        <stop offset="1" stop-color="#1fb6ea"/>
      </linearGradient>
    </defs>
    <polygon points="0,0 620,0 620,150 0,250" fill="url(#skyTone)"/>
    <polygon points="0,250 620,150 620,379 0,379" fill="#12a54e"/>
  </svg>
  <div class="brand">
    <span class="brand-mark"></span>
    <span class="brand-name">Tindarra Stud</span>
  </div>
  <div class="cattle-illustration" role="img" aria-label="Illustration of a white bull standing in a green paddock with a tree line behind"></div>
</section>

<section class="card card-back">
  <div class="brand">
    <span class="brand-mark"></span>
    <span class="brand-name">Tindarra Stud</span>
  </div>
  <div class="holder">Dean Hockley</div>
  <div class="divider"></div>
  <ul class="contacts">
    <li><span class="contact-icon"><svg viewBox="0 0 12 12"><path d="M3 1 L5 3 L4 4.5 Q5 7 7.5 8 L9 7 L11 9 L9.5 11 Q2 9.5 1 2.5 Z" fill="#fff"/></svg></span>07 49372058</li>
    <li><span class="contact-icon"><svg viewBox="0 0 12 12"><rect x="3.5" y="1" width="5" height="10" rx="1" fill="none" stroke="#fff" stroke-width="1.2"/><circle cx="6" cy="9.2" r="0.7" fill="#fff"/></svg></span>0417295846</li>
    <li><span class="contact-icon"><svg viewBox="0 0 12 12"><rect x="1" y="3" width="10" height="6.5" fill="none" stroke="#fff" stroke-width="1.1"/><path d="M1 3 L6 7 L11 3" fill="none" stroke="#fff" stroke-width="1.1"/></svg></span>drhock@fencelinemail.com.au</li>
    <li><span class="contact-icon blank"></span>PO Box 318 Wirralong Qld 4791</li>
    <li><span class="contact-icon blank"></span>57 Hockley's Rd Old Tindarra Qld 4791</li>
  </ul>
  <div class="back-strip"></div>
</section>

</body>
</html>
```